Brindlewick Music Studio needs a promotional postcard design

We are looking for a postcard design for a small business that provides clients with private music lesson instruction. We are looking for a design that will convey the message of "music is fun for kids" that will appeal to parents and encourage them to sign up. We have a company logo that should be used and our color scheme is teal and turquoise. All of our contact info should be displayed as well.

Target Market(s)

Parents with young kids

Contact Information for Business Card

web: www.brindlewickmusicstudio.example
email: lessons@brindlewickmusicstudio.example
phone: 202-555-0147

Font styles to use
Serif
Sans Serif

Colors
33b8a4
86cfc6
0456a4
87cfc6

Requirements
Must have
• Music lessons in your home
• Creating little stars one at a time
• Sign Up Now
• Please use these images:
Nice to have
• Something like this sample postcard:

```html
<!DOCTYPE html>
<html lang="en">
<head>
<meta charset="utf-8">
<title>Brindlewick Music Studio – Postcard</title>
<link rel="stylesheet" href="https://fonts.googleapis.com/css2?family=Marcellus&family=Oswald:wght@300;400&display=swap">
<style>
  :root{
    --stage:#e6e7e8;
    --teal:#4db8bd;
    --teal-ink:#3fafb2;
    --ink:#1d1d1d;
    --paper:#f6f6f6;
    --white:#ffffff;
    --rule:#8a8a8a;
    --stamp:#dcdcdc;
  }
  *{box-sizing:border-box;margin:0;padding:0}
  html,body{width:1200px;height:802px;overflow:hidden;background:var(--stage)}
  .stage{position:relative;width:1200px;height:802px}
  .postcard{position:absolute;top:233px;width:560px;height:335px;background:var(--paper);
    box-shadow:0 3px 8px rgba(0,0,0,.28);overflow:hidden}
  .postcard--front{left:20px}
  .postcard--back{left:620px;background:var(--white)}

  /* front */
  .hero-photo{position:absolute;left:0;top:0;width:257px;height:335px;
    background:
      radial-gradient(ellipse 70px 120px at 120px 90px, rgba(196,150,128,.55), rgba(196,150,128,0) 100%),
      radial-gradient(ellipse 85px 150px at 125px 210px, rgba(22,70,60,.9), rgba(22,70,60,0) 100%),
      linear-gradient(180deg, rgba(0,0,0,0) 84%, rgba(62,150,140,.55) 88%, rgba(0,0,0,0) 92%),
      linear-gradient(180deg,#0a0a0a 0%,#121212 86%,#cfc7bc 93%,#e6e0d8 100%)}
  .inset-photo{position:absolute;left:179px;top:138px;width:107px;height:147px;
    background:var(--white);padding:6px}
  .inset-photo span{display:block;width:100%;height:100%;
    background:
      radial-gradient(ellipse 30px 36px at 55px 55px, rgba(214,170,150,.8), rgba(214,170,150,0) 100%),
      linear-gradient(160deg,#6a5a4e,#2b2522)}
  .brand{position:absolute;left:294px;top:37px;display:flex;align-items:center;gap:17px}
  .brand__dot{width:70px;height:70px;border-radius:50%;background:var(--teal)}
  .brand__name{font-family:"Marcellus",serif;font-weight:400;color:var(--teal-ink);line-height:1}
  .brand__name .line1{display:block;font-size:30px}
  .brand__name .line2{display:block;font-size:10px;letter-spacing:5.5px;margin-top:9px}
  .headline{position:absolute;left:286px;width:274px;top:141px;text-align:center;
    font-family:"Marcellus",serif;font-weight:400;font-size:40px;line-height:54px;color:var(--ink)}
  .headline .accent{color:var(--teal-ink)}

  /* back */
  .contact-panel{position:absolute;left:0;top:0;width:304px;height:335px;background:var(--teal)}
  .snap{position:absolute;width:98px;height:104px;background:var(--white);padding:2px}
  .snap span{display:block;width:100%;height:100%}
  .snap--group{left:17px;top:22px}
  .snap--group span{background:
      radial-gradient(ellipse 40px 20px at 50px 70px, rgba(90,140,150,.6), rgba(90,140,150,0) 100%),
      linear-gradient(180deg,#2a1e1c,#6b4a3c)}
  .snap--piano{left:104px;top:44px}
  .snap--piano span{background:
      radial-gradient(ellipse 22px 34px at 40px 62px, rgba(235,235,240,.8), rgba(235,235,240,0) 100%),
      linear-gradient(180deg,#0e1220,#3a3d4a)}
  .snap--recital{left:188px;top:96px}
  .snap--recital span{background:
      radial-gradient(ellipse 24px 22px at 35px 62px, rgba(200,40,40,.75), rgba(200,40,40,0) 100%),
      linear-gradient(180deg,#5a3420,#8a4a2a)}
  .contact-list{position:absolute;left:13px;top:204px;list-style:none}
  .contact-list li{display:flex;align-items:center;height:36px;gap:7px;
    font-family:"Oswald",sans-serif;font-weight:300;font-size:18px;letter-spacing:-.3px;
    color:var(--white);white-space:nowrap}
  .contact-list li svg{flex:none}
  .stamp-box{position:absolute;left:458px;top:41px;width:67px;height:69px;background:var(--stamp)}
  .address-line{position:absolute;left:339px;width:189px;height:1px;background:var(--rule)}
  .address-line--1{top:178px}
  .address-line--2{top:214px}
  .address-line--3{top:250px}
  .address-line--4{top:288px}
</style>
</head>
<body>
<main class="stage">

  <section class="postcard postcard--front" aria-label="Postcard front">
    <div class="hero-photo" role="img" aria-label="Photo of a young girl in a dark green dress playing the violin on stage"></div>
    <div class="inset-photo"><span role="img" aria-label="Photo of a smiling child making a peace sign"></span></div>
    <div class="brand">
      <div class="brand__dot"></div>
      <div class="brand__name"><span class="line1">Brindlewick</span><span class="line2">MUSIC STUDIO</span></div>
    </div>
    <h1 class="headline"><span class="accent">MUSIC</span><br>IS FUN<br>FOR KIDS</h1>
  </section>

  <section class="postcard postcard--back" aria-label="Postcard back">
    <div class="contact-panel">
      <div class="snap snap--group"><span role="img" aria-label="Photo of a group of young students with their teacher"></span></div>
      <div class="snap snap--piano"><span role="img" aria-label="Photo of a girl in a white dress playing the piano"></span></div>
      <div class="snap snap--recital"><span role="img" aria-label="Photo of a child at a piano recital"></span></div>
      <ul class="contact-list">
        <li class="phone">
          <svg width="28" height="28" viewBox="0 0 28 28"><circle cx="14" cy="14" r="13" fill="#fff"/>
            <path d="M10 8.5c.8-.6 1.6-.4 2 .4l1 2c.3.7.1 1.2-.5 1.6l-.6.4c.6 1.5 1.7 2.7 3.2 3.3l.4-.6c.4-.6 1-.8 1.6-.5l2 1c.8.4 1 1.2.4 2-1 1.3-2.4 1.6-4 .9-3-1.3-5.1-3.5-6.4-6.5-.7-1.6-.3-3 .9-4z" fill="#4db8bd"/></svg>
          202-555-0147
        </li>
        <li class="mail">
          <svg width="28" height="28" viewBox="0 0 28 28"><circle cx="14" cy="14" r="13" fill="#fff"/>
            <rect x="8" y="9.5" width="12" height="9" rx="1" fill="none" stroke="#4db8bd" stroke-width="1.6"/>
            <path d="M8.5 10.5 14 15l5.5-4.5" fill="none" stroke="#4db8bd" stroke-width="1.6"/></svg>
          lessons@brindlewickmusicstudio.example
        </li>
        <li class="web">
          <svg width="28" height="28" viewBox="0 0 28 28"><circle cx="14" cy="14" r="13" fill="#fff"/>
            <circle cx="14" cy="14" r="6.5" fill="none" stroke="#4db8bd" stroke-width="1.6"/>
            <ellipse cx="14" cy="14" rx="2.8" ry="6.5" fill="none" stroke="#4db8bd" stroke-width="1.3"/>
            <path d="M7.5 14h13" stroke="#4db8bd" stroke-width="1.3"/></svg>
          www.brindlewickmusicstudio.example
        </li>
      </ul>
    </div>
    <div class="stamp-box"></div>
    <div class="address-line address-line--1"></div>
    <div class="address-line address-line--2"></div>
    <div class="address-line address-line--3"></div>
    <div class="address-line address-line--4"></div>
  </section>

</main>
</body>
</html>
```